National online rug retailer needs a home page design

See the LoomNest logo and create a home page design around that color theme. Details are spelled out in word document uploaded below.
Updates

Apparently this website did not take my attachement showing the logo and basic requirements.  If you would send me your email address, I will send you the attachment directly.
Best regards,
Ned Carver
ncarver@qwplex.com

Target Market(s)

The target market is home owners 25 to 75 years old with combined incomes over $100,000 per year.

Industry/Entity Type

Online

Requirements
Must have
• Lots of white space with black letters and creative use of red and possibly one other color. Would like a compelling call to action button.

```html
<!DOCTYPE html>
<html lang="en">
<head>
<meta charset="utf-8">
<title>LoomNest – Home</title>
<link href="https://fonts.googleapis.com/css2?family=Exo+2:wght@400;500;600&family=Arimo:wght@400;700&display=swap" rel="stylesheet">
<style>
:root{
  --red:#d41a1f;
  --red-dark:#b5121a;
  --ink:#333;
  --grey:#666;
  --line:#cfcfcf;
  --panel:#efefef;
  --page:#f7f7f7;
  --footer:#f1efea;
  --green:#3cb521;
}
*{box-sizing:border-box;margin:0;padding:0}
html,body{width:900px;height:1200px;overflow:hidden}
body{position:relative;background:var(--page);font-family:"Arimo",Arial,sans-serif;color:var(--ink)}
.abs{position:absolute;white-space:nowrap}
a{color:inherit;text-decoration:none}

/* header */
.logo{left:152px;top:44px;display:flex;align-items:center;gap:6px}
.logo-mark{width:13px;height:13px;background:var(--red)}
.logo-name{font-family:"Exo 2",sans-serif;font-weight:500;font-size:21px;color:var(--red);line-height:1}
.tagline{left:202px;top:74px;font-size:7px;color:var(--grey)}
.cartbar{right:150px;top:27px;font-size:7px;color:var(--grey)}
.cartbar b{color:var(--red)}
.phone{right:150px;top:46px;font-size:10px;color:var(--ink)}
.phone b{color:var(--red)}
.search{left:330px;top:61px;width:228px;height:21px;border:1px solid var(--line);background:#fafafa;font-size:7px;color:#aaa;padding:6px 8px}
.search svg{position:absolute;right:6px;top:4px}
.search::after{content:"";position:absolute;right:24px;top:2px;bottom:2px;border-left:1px solid var(--line)}
.account{left:573px;top:71px;font-size:7px;color:var(--red)}
.chat{left:660px;top:70px;font-size:7px;color:var(--ink);display:flex;align-items:center;gap:4px}
.dot{width:8px;height:8px;border-radius:50%;display:inline-block}
.chat .on{color:var(--green)}

/* nav */
.nav{left:150px;top:102px;width:600px;height:25px;border:1px solid var(--line);border-radius:3px;background:linear-gradient(#fdfdfd,#ececec);display:flex;align-items:center;padding-left:8px}
.nav a{font-family:"Exo 2",sans-serif;font-size:8.5px;color:#444;padding:0 12px;border-right:1px dotted #bbb}
.nav a:last-of-type{border-right:0}
.social{position:absolute;right:5px;top:5px;display:flex;gap:4px}
.social span{width:14px;height:14px;border:1px solid var(--line);background:#fff;font-size:7px;display:flex;align-items:center;justify-content:center;color:#555}

/* sidebars */
.panel{background:var(--panel);border:1px solid #dcdcdc;border-radius:4px}
.cats{left:150px;top:134px;width:132px;height:230px}
.panel-title{margin:5px 6px 0;height:15px;border:1px solid #ccc;background:#fff;font-family:"Exo 2",sans-serif;font-size:9px;color:var(--red);text-align:center;line-height:13px}
.cats ul{list-style:none;margin:12px 0 0 8px;font-size:7.5px;line-height:12px;color:#555}
.cats li.sub{padding-left:7px}
.likes{left:619px;top:134px;width:131px;height:230px}
.like{position:absolute;left:13px;width:102px}

/* banner */
.banner-top{left:285px;top:135px;width:330px;height:126px;background:linear-gradient(135deg,#3a2a35,#8e2a2a 45%,#c9b9a6 70%,#6b2026)}
.banner-bot{left:285px;top:264px;width:330px;height:98px;background:linear-gradient(90deg,#5a3a25,#b59a70 35%,#3b2a1e 65%,#6e4a2c)}
.banner-cta{left:285px;top:320px;width:330px;height:42px;background:var(--red);font-family:"Exo 2",sans-serif;color:#fff;font-size:15px;line-height:18px;overflow:hidden}
.banner-cta span{position:absolute;white-space:nowrap}

.divider{left:0;top:383px;width:900px;border-top:1px dashed #aaa}
.section-title{left:152px;top:401px;font-family:"Exo 2",sans-serif;font-weight:500;font-size:18px;color:var(--red)}

/* products */
.card{border:2px solid var(--red);overflow:hidden}
.card .caption{position:absolute;left:0;right:0;bottom:0;height:24px;background:rgba(50,50,50,.75);color:#fff;font-family:"Exo 2",sans-serif;display:flex;align-items:center;justify-content:center;font-size:14px}
.card .caption.big{font-size:19px;font-weight:500;height:26px}
.desc{font-size:7px;line-height:8.5px;color:#555;width:145px;white-space:normal}
.arrow{width:10px;height:14px}

/* trust */
.badge{top:970px;height:22px;background:#e2e2e2;border:1px solid #c8c8c8}
.badge.round{border-radius:50%;background:#e9d98a;border-color:#c8b560}

/* footer */
.footer{left:0;top:1025px;width:900px;height:140px;background:var(--footer);border-top:1px dashed #ddd}
.fcol h3{font-family:"Exo 2",sans-serif;font-weight:500;font-size:9.5px;color:var(--red);margin-bottom:11px}
.fcol ul{list-style:none;font-size:6.5px;font-weight:700;line-height:10px;color:#444}
.signup{left:536px;top:1058px;font-family:"Exo 2",sans-serif;font-size:8px;color:var(--red)}
.email{left:536px;top:1077px;width:166px;height:18px;border:1px solid #ccc;border-radius:3px;background:#fff;font-size:7px;color:#999;padding:5px 8px}
.submit{left:660px;top:1100px;width:42px;height:12px;background:#999;color:#fff;font-size:7px;text-align:center;line-height:12px;border-radius:2px}
.follow{left:537px;top:1146px;font-family:"Exo 2",sans-serif;font-weight:500;font-size:12px;color:var(--red)}
.fsocial{left:615px;top:1145px;display:flex;gap:9px}
.fsocial span{width:14px;height:14px;border:1px solid var(--line);background:#fff;font-size:7px;display:flex;align-items:center;justify-content:center;color:#555}
.copy{left:0;top:1165px;width:900px;height:35px;background:var(--red);color:#fff;font-size:7px;padding:12px 0 0 151px}
</style>
</head>
<body>

<!-- header -->
<div class="abs logo"><span class="logo-mark"></span><span class="logo-name">LoomNest.com</span></div>
<div class="abs tagline">for domestic and heirloom values</div>
<div class="abs cartbar">Items: <b>0</b> | Total: $0.00 View Cart | Check Out</div>
<div class="abs phone">Order toll-free: <b>1-888-555-0147</b></div>
<div class="abs search">Enter key words or item #
  <svg width="10" height="10" viewBox="0 0 10 10"><circle cx="4" cy="4" r="3" fill="none" stroke="#555" stroke-width="1.3"/><line x1="6.2" y1="6.2" x2="9" y2="9" stroke="#555" stroke-width="1.5"/></svg>
</div>
<div class="abs account">My Account | Sign In</div>
<div class="abs chat"><span class="dot" style="background:#333"></span>Live Chat | <span class="dot" style="background:var(--green)"></span><span class="on">Online</span></div>

<nav class="abs nav">
  <a>Home</a><a>Selection Guides</a><a>Rug Care</a><a>FAQ</a><a>Return Policy</a><a>Free Shipping</a><a>Clearance Rugs</a>
  <div class="social"><span>f</span><span>t</span><span>in</span><span>g+</span></div>
</nav>

<!-- categories -->
<aside class="abs panel cats">
  <div class="panel-title">Categories</div>
  <ul>
    <li>- RUG THEME</li><li class="sub">- Traditioal</li><li class="sub">- Transitional</li><li class="sub">- Casual</li>
    <li>- COLOR WAY</li><li class="sub">- Black</li><li class="sub">- Green</li><li class="sub">- Gold</li>
    <li>+ SIZE</li><li>+ SHAPE</li><li>+ FIBER CONTANT</li><li>+ MFGR. BRAND</li><li>+ MFGR. COLLECTION</li><li>+ PRICE</li>
  </ul>
</aside>

<!-- banner -->
<div class="abs banner-top" role="img" aria-label="Close-up photo of patterned red oriental rugs with fringe"></div>
<div class="abs banner-bot" role="img" aria-label="Photo of assorted patterned rug swatches"></div>
<div class="abs banner-cta"><span style="left:11px;top:3px">SAVE UP TO 20% OFF</span><span style="right:12px;top:21px">ON THIS SUMMER</span></div>

<!-- you may also like -->
<aside class="abs panel likes">
  <div class="panel-title">You May Also Like</div>
  <div class="like" role="img" aria-label="Photo of a multicolour geometric triangle rug" style="top:32px;height:96px;background:linear-gradient(135deg,#f26a1b,#b9c23a 40%,#2b87c8 65%,#e23b2a)"></div>
  <div class="like" role="img" aria-label="Photo of rolled teal and orange rugs on yellow" style="top:141px;height:90px;background:linear-gradient(135deg,#f0d21c,#3fa6a6 45%,#e08a2a 75%,#f0d21c)"></div>
</aside>

<div class="abs divider"></div>
<h2 class="abs section-title">OUR PRODUCTS</h2>

<!-- arrows -->
<svg class="abs arrow" style="left:150px;top:500px" viewBox="0 0 10 14"><polyline points="8,1 2,7 8,13" fill="none" stroke="var(--red)" stroke-width="2.2"/></svg>
<svg class="abs arrow" style="left:737px;top:500px" viewBox="0 0 10 14"><polyline points="2,1 8,7 2,13" fill="none" stroke="var(--red)" stroke-width="2.2"/></svg>
<svg class="abs arrow" style="left:150px;top:680px" viewBox="0 0 10 14"><polyline points="8,1 2,7 8,13" fill="none" stroke="var(--red)" stroke-width="2.2"/></svg>
<svg class="abs arrow" style="left:737px;top:680px" viewBox="0 0 10 14"><polyline points="2,1 8,7 2,13" fill="none" stroke="var(--red)" stroke-width="2.2"/></svg>
<svg class="abs arrow" style="left:150px;top:836px" viewBox="0 0 10 14"><polyline points="8,1 2,7 8,13" fill="none" stroke="var(--red)" stroke-width="2.2"/></svg>
<svg class="abs arrow" style="left:737px;top:836px" viewBox="0 0 10 14"><polyline points="2,1 8,7 2,13" fill="none" stroke="var(--red)" stroke-width="2.2"/></svg>

<!-- row 1 -->
<div class="abs card" style="left:178px;top:444px;width:144px;height:127px">
  <div role="img" aria-label="Photo of a modern striped-border rug" style="width:100%;height:100%;background:linear-gradient(135deg,#2c2a6b,#c23a3a 35%,#c7b89a 60%)"></div>
  <div class="caption big">MODREN</div></div>
<p class="abs desc" style="left:180px;top:575px">Lorem ipsum dolor sit amet, consectetuer adipiscing elit, sed diam nonummy nibh euismod.</p>

<div class="abs card" style="left:382px;top:444px;width:143px;height:127px">
  <div role="img" aria-label="Photo of a traditional patchwork rug" style="width:100%;height:100%;background:linear-gradient(135deg,#4a2e1e,#8b6a3e 40%,#3a2418 70%,#7d4a2a)"></div>
  <div class="caption big">TRADITIONAL</div></div>
<p class="abs desc" style="left:384px;top:575px">Lorem ipsum dolor sit amet, consectetuer adipiscing elit, sed diam nonummy nibh euismod.</p>

<div class="abs card" style="left:586px;top:444px;width:134px;height:127px">
  <div role="img" aria-label="Photo of a grey shag rug under a table" style="width:100%;height:100%;background:linear-gradient(#c8a27a,#9a9a9a 25%,#6d6d6d)"></div>
  <div class="caption big">Transitional</div></div>
<p class="abs desc" style="left:586px;top:575px">Lorem ipsum dolor sit amet, consectetuer adipiscing elit, sed diam nonummy nibh euismod.</p>

<!-- row 2 -->
<div class="abs card" style="left:177px;top:622px;width:143px;height:126px">
  <div role="img" aria-label="Photo of a geometric triangle rug" style="width:100%;height:100%;background:linear-gradient(135deg,#f26a1b,#b9c23a 40%,#2b87c8 65%,#e23b2a)"></div>
  <div class="caption">Lorem ipsum dolor</div></div>
<p class="abs desc" style="left:178px;top:753px">Lorem ipsum dolor sit amet, consectetuer adipiscing elit, sed diam nonummy nibh euismod.</p>

<div class="abs card" style="left:384px;top:627px;width:139px;height:123px">
  <div role="img" aria-label="Photo of a bright room with a colourful rug" style="width:100%;height:100%;background:linear-gradient(#f4f4f4,#dcdcdc 60%,#6a5a8a)"></div>
  <div class="caption">Lorem ipsum dolor</div></div>
<p class="abs desc" style="left:385px;top:756px">Lorem ipsum dolor sit amet, consectetuer adipiscing elit, sed diam nonummy nibh euismod.</p>

<div class="abs card" style="left:586px;top:627px;width:117px;height:126px">
  <div role="img" aria-label="Photo of a pink and black striped rug" style="width:100%;height:100%;background:linear-gradient(#3a1f2a,#e9c3d0 40%,#2a1a20 70%,#e9c3d0)"></div>
  <div class="caption" style="font-size:11px">Lorem ipsum dolor</div></div>
<p class="abs desc" style="left:586px;top:756px;width:112px">Lorem ipsum dolor sit amet, consectetuer adipiscing elit, sed diam nonummy nibh euismod.</p>

<!-- row 3 -->
<div class="abs card" style="left:177px;top:798px;width:143px;height:89px">
  <div role="img" aria-label="Photo of a rolled colourful rug" style="width:100%;height:100%;background:linear-gradient(135deg,#7a7a7a,#2bb0d8 40%,#e23a4a 70%,#f2f2f2)"></div>
  <div class="caption">Lorem ipsum dolor</div></div>
<p class="abs desc" style="left:178px;top:893px">Lorem ipsum dolor sit amet, consectetuer adipiscing elit, sed diam nonummy nibh euismod.</p>

<div class="abs card" style="left:384px;top:798px;width:139px;height:89px">
  <div role="img" aria-label="Photo of a child's room with a star rug" style="width:100%;height:100%;background:linear-gradient(#dfe6ec,#e8e2d6 40%,#2e3f6e 60%)"></div>
  <div class="caption">Lorem ipsum dolor</div></div>
<p class="abs desc" style="left:386px;top:893px">Lorem ipsum dolor sit amet, consectetuer adipiscing elit, sed diam nonummy nibh euismod.</p>

<div class="abs card" style="left:586px;top:798px;width:116px;height:89px">
  <div role="img" aria-label="Photo of a red rug with coloured dots" style="width:100%;height:100%;background:radial-gradient(circle at 50% 40%,#f0c040,#d61f1f 55%,#8a1010)"></div>
  <div class="caption" style="font-size:11px">Lorem ipsum dolor</div></div>
<p class="abs desc" style="left:586px;top:893px;width:112px">Lorem ipsum dolor sit amet, consectetuer adipiscing elit, sed diam nonummy nibh euismod.</p>

<!-- trust & payment badges -->
<div class="abs badge" style="left:220px;width:40px;top:972px;height:16px"></div>
<div class="abs badge round" style="left:272px;width:28px;top:966px;height:28px"></div>
<div class="abs badge round" style="left:316px;width:34px;top:965px;height:30px;background:#e4e0a0"></div>
<div class="abs badge" style="left:364px;width:41px;top:971px;height:22px;background:#2d6aa8"></div>
<div class="abs badge" style="left:418px;width:48px;top:970px;height:24px;background:#e8e8e8"></div>
<div class="abs badge" style="left:481px;width:26px;top:972px;height:16px;background:#2a4a9a"></div>
<div class="abs badge" style="left:511px;width:24px;top:972px;height:16px;background:#f0a030"></div>
<div class="abs badge" style="left:540px;width:25px;top:972px;height:16px;background:#f4f4f4"></div>
<div class="abs badge" style="left:569px;width:25px;top:972px;height:16px;background:#3a86c8"></div>
<div class="abs badge" style="left:598px;width:25px;top:972px;height:16px;background:#eef2f6"></div>
<div class="abs badge" style="left:628px;width:25px;top:972px;height:16px;background:#f2f2f2"></div>

<!-- footer -->
<footer class="abs footer"></footer>
<div class="abs fcol" style="left:152px;top:1036px">
  <h3>Customer Service</h3>
  <ul><li>Shipping</li><li>Return Policy</li><li>Privacy Policy</li><li>Ordering &amp; Delivery Checklist</li><li>Terms of Use</li><li>Terms of Sale</li><li>Contact Us</li><li>Environmental Policy</li></ul>
</div>
<div class="abs fcol" style="left:281px;top:1036px">
  <h3>Resources</h3>
  <ul><li>Product Articles</li><li>Learning Center</li><li>Help</li><li>Refer A Friend</li><li>LoomNest Blog</li><li>Room Scene Viewer</li><li>Site Map</li><li>FAQ</li><li>Customer Testimonials</li><li>Photo Gallery</li></ul>
</div>
<div class="abs fcol" style="left:386px;top:1036px">
  <h3>Corporate Info</h3>
  <ul><li>About LoomNest.com</li><li>Careers</li><li>Affiliates</li></ul>
</div>
<div class="abs signup">Sign up for Daily Fair Deals. Don't miss out!</div>
<div class="abs email">Enter Your Email Address</div>
<div class="abs submit">SUBMIT ›</div>
<div class="abs follow">Follow Us</div>
<div class="abs fsocial"><span>f</span><span>t</span><span>in</span><span>g+</span></div>
<div class="abs copy">©1998-2013 LoomNest.com Inc. All rights reserved.</div>

</body>
</html>
```